Homes, Invest in Non-performing loans

We need only 3 web pages, one for the home, one for the content, one for the properties.
The main focus of our business is to offer non performing loans (before foreclosures) to the general public. All the non-performing mortgages will end in a house, an apartment, a store, etc.
Our customers are able to invest from 10,000usd to 1,000,000usd (average 50,000usd).
Our customers' usual focus groups are employees who want second earnings, perceiving the business feeling without outlay time. They look for a solid finance sense corporation that confers them certainty.
Nearly all our clients desire the house, apartment, store, etc. more than the actual earnings.
The name of our company is BRAMLEY
Reason: We value the time and effort you already invest in our project. We realize that we did't come back on some of the doubts requested by the designers. It will be inequitable to the designers who prerequisite our feedback. We also appreciate the comprehension of the community in this postponement.
Reason: Designers,
We really apreciate all the time and effort you put on our project. From the begining we ask for 3 pages, so now we will leave the 10 finalist and provide some extra time to submit the other 2 pages.
We will race the price in 10%
Target Market(s)
Our customers average investors works as employees and want to have a second income or business without spending time. (People from 35 to 50)
Industry/Entity Type
Finance
Requirements
Should not have
- FLASH

```html
<!DOCTYPE html>
<html lang="en">
<head>
<meta charset="utf-8">
<title>Bramley — Non-performing loans</title>
<link rel="stylesheet" href="https://fonts.googleapis.com/css2?family=Roboto+Condensed:wght@300;400;700&family=Arimo:wght@400;700&display=swap">
<style>
:root{
  --olive:#7d7d1f;
  --olive-dark:#5f5f12;
  --blue:#0b7fd9;
  --link-blue:#2a62b8;
  --ink:#222;
  --muted:#555;
  --page:#f4f4f4;
  --green-a:#8dba22;
  --green-b:#5b8d10;
  --slate:#343a46;
  --orange:#e64a12;
  --panel:#ebebeb;
  --footer:#2a2a2a;
  --footer-text:#b8b8b8;
}
*{margin:0;padding:0;box-sizing:border-box}
html,body{width:1200px;height:1125px;overflow:hidden;background:var(--page)}
body{font-family:"Arimo",Arial,sans-serif;color:var(--ink)}
.stage{position:relative;width:1280px;height:1200px;transform:scale(.9375);transform-origin:0 0;background:var(--page);overflow:hidden}
.abs{position:absolute}
.cond{font-family:"Roboto Condensed","Arial Narrow",sans-serif}

/* header */
.site-header{left:0;top:0;width:1280px;height:142px;background:#fff}
.header-rule{left:0;top:142px;width:1280px;height:6px;background:var(--olive)}
.brand{left:150px;top:58px;font-family:"Roboto Condensed",sans-serif;font-weight:700;font-size:46px;color:#2b2b2b;letter-spacing:1px;display:flex;align-items:center;gap:10px}
.brand-mark{width:22px;height:22px;background:var(--olive)}
.advisor{left:821px;top:34px;width:309px;height:35px;border-radius:18px;background:var(--blue);color:#fff;font-size:17px;display:flex;align-items:center;justify-content:center;gap:18px}
.main-nav{left:597px;top:106px;height:36px;display:flex;font-size:15px;text-transform:uppercase}
.main-nav a{color:#222;text-decoration:none;display:flex;align-items:center;height:36px;padding-top:2px}
.main-nav .is-current{width:100px;justify-content:center;color:#fff;background:linear-gradient(#8a8a28,var(--olive-dark));margin-right:37px}
.main-nav .gap-40{margin-right:40px}

/* hero */
.hero{left:0;top:148px;width:1280px;height:468px;background:radial-gradient(ellipse at 58% 30%,#6a82c9 0%,#4a4f9a 35%,#2b2a63 70%,#1d1c48 100%)}
.hero-figure{left:240px;top:250px;width:890px;height:366px;background:linear-gradient(90deg,rgba(214,80,40,.55),rgba(140,190,60,.45) 35%,rgba(180,200,225,.55) 55%,rgba(170,195,230,.5));border-radius:40px 40px 0 0}
.hero-caption{right:157px;top:196px;color:#fff;font-weight:300;font-size:25px}
.hero-arrow{top:389px;width:30px;height:30px}

/* products */
.product-title{top:643px;font-size:16px}
.product-card{top:668px;width:150px;height:106px;background:#fff;border:4px solid #ddd;box-shadow:0 0 0 1px #c8c8c8;font-size:12px;line-height:18px;color:var(--muted);text-align:center;padding:12px 10px}
.more{top:781px;font-size:11px;color:var(--link-blue);text-transform:uppercase}
.offer-title{left:151px;top:811px;font-size:15px}
.offer-list{left:153px;top:839px;list-style:none;font-size:12.5px}
.offer-list li{height:28px;display:flex;align-items:center;gap:8px;margin-top:-6px;padding-top:6px}

/* announcements */
.news{left:660px;top:660px;width:470px;height:254px;background:linear-gradient(135deg,var(--green-a),var(--green-b))}
.news-bar{left:651px;top:678px;width:479px;height:32px;background:var(--slate);color:#fff;font-size:16px;font-weight:300;padding:5px 0 0 15px}
.news-item{left:678px;width:445px;color:#fff}
.news-item h3{font-family:"Roboto Condensed",sans-serif;font-weight:400;font-size:14.5px;color:#16240a;margin-bottom:4px}
.news-item p{font-size:12px;line-height:16px}
.news-item time{display:block;font-size:11px;margin-top:6px}
.read-all{font-size:11px;text-transform:uppercase;text-decoration:underline}

/* bottom panels */
.footer{left:0;top:1085px;width:1280px;height:115px;background:var(--footer)}
.panel{top:960px;height:155px;background:var(--panel)}
.tab{top:960px;width:98px;height:155px;background:var(--orange);color:#fff;font-size:14px;line-height:17px}
.tab-pointer{top:1002px;width:0;height:0;border-top:6px solid transparent;border-bottom:6px solid transparent;border-left:10px solid var(--orange)}
.quote{left:268px;top:978px;width:335px;font-size:12.5px;line-height:20px;color:#444}
.quote-by{right:675px;top:1081px;font-size:12.5px}
.promise{font-size:27px;font-weight:300;color:#333}
.cta{left:931px;top:1070px;width:186px;height:35px;border-radius:18px;background:var(--blue);color:#fff;font-size:17px;display:flex;align-items:center;justify-content:center;gap:14px}
.cta-icon{width:15px;height:15px;border-radius:50%;background:#fff;display:flex;align-items:center;justify-content:center}

/* footer */
.footer-links{left:151px;top:1140px;font-size:12.5px;color:var(--footer-text);word-spacing:3px}
.copyright{left:151px;top:1161px;font-size:12.5px;color:var(--footer-text);word-spacing:3px}
.social{top:1144px;width:30px;height:30px;border-radius:50%;background:#e6e6e6;box-shadow:0 0 0 2px #bbb inset}
</style>
</head>
<body>
<div class="stage">

  <header class="site-header abs"></header>
  <div class="header-rule abs"></div>
  <div class="brand abs"><span class="brand-mark"></span>BRAMLEY</div>
  <div class="advisor abs cond"><span>Talk with our advisor</span><span>+1 555 014 2290</span></div>
  <nav class="main-nav abs cond">
    <a class="is-current" href="#">Home</a>
    <a class="gap-40" href="#">Buy</a>
    <a class="gap-40" href="#">Sell</a>
    <a class="gap-40" href="#">About</a>
    <a class="gap-40" href="#">Testimonials</a>
    <a href="#">Contact</a>
  </nav>

  <section class="hero abs">
  </section>
  <div class="hero-figure abs" role="img" aria-label="Photo of a smiling three-generation family beside a rising colourful bar chart"></div>
  <p class="hero-caption abs cond">Nam dapibus nulla quis lorem accumsan pretium. Maecenas tincidunt luctus...</p>
  <svg class="hero-arrow abs" style="left:5px" viewBox="0 0 30 30"><circle cx="15" cy="15" r="15" fill="#8a8a9a" fill-opacity=".7"/><path d="M17 9l-6 6 6 6" stroke="#333" stroke-width="1.5" fill="none"/></svg>
  <svg class="hero-arrow abs" style="left:1245px" viewBox="0 0 30 30"><circle cx="15" cy="15" r="15" fill="#8a8a9a" fill-opacity=".7"/><path d="M13 9l6 6-6 6" stroke="#333" stroke-width="1.5" fill="none"/></svg>

  <h2 class="product-title abs cond" style="left:153px;font-weight:400">Buy a Loan</h2>
  <h2 class="product-title abs cond" style="left:320px;font-weight:400">Sell a Loan</h2>
  <h2 class="product-title abs cond" style="left:488px;font-weight:400">Fund a Loan</h2>
  <div class="product-card abs" style="left:153px">Lorem ipsum dolor sit amet, consectetur adipiscing elit. Nullam dui tellus...</div>
  <div class="product-card abs" style="left:320px">Lorem ipsum dolor sit amet, consectetur adipiscing elit. Nullam dui tellus...</div>
  <div class="product-card abs" style="left:488px">Lorem ipsum dolor sit amet, consectetur adipiscing elit. Nullam dui tellus...</div>
  <a class="more abs" style="left:214px">Findout more...</a>
  <a class="more abs" style="left:381px">Findout more...</a>
  <a class="more abs" style="left:549px">Findout more...</a>

  <h2 class="offer-title abs cond" style="font-weight:400">What can you do with Us?</h2>
  <ul class="offer-list abs">
    <li><svg width="13" height="13" viewBox="0 0 13 13"><circle cx="6.5" cy="6.5" r="6" fill="#eee" stroke="#aaa"/><path d="M5 4l3.5 2.5L5 9z" fill="#777"/></svg>Posuere luctus arcu. Fusce accumsa</li>
    <li><svg width="13" height="13" viewBox="0 0 13 13"><circle cx="6.5" cy="6.5" r="6" fill="#eee" stroke="#aaa"/><path d="M5 4l3.5 2.5L5 9z" fill="#777"/></svg>Consectetur adipiscing elit. Nullam dui</li>
    <li><svg width="13" height="13" viewBox="0 0 13 13"><circle cx="6.5" cy="6.5" r="6" fill="#eee" stroke="#aaa"/><path d="M5 4l3.5 2.5L5 9z" fill="#777"/></svg>Lorem ipsum dolor sit amet, consectetur adipiscing</li>
  </ul>

  <section class="news abs"></section>
  <div class="news-bar abs cond">Announcements</div>
  <article class="news-item abs" style="top:722px">
    <h3>Lorem ipsum dolor sit amet, consectetur adipiscing elit.</h3>
    <p>Lorem ipsum dolor sit amet, consectetur adipiscing elit. Nullam dui tellus, varius vel luctus nec, posuere luctus arcu. Fusce accumsan neque vel augue...</p>
    <time>On Dec 15, 2012</time>
  </article>
  <article class="news-item abs" style="top:814px">
    <h3>Lorem ipsum dolor sit amet, consectetur adipiscing elit.</h3>
    <p>KHNit amet, consectetur adipiscing elit. Nullam dui tellus, luctus nec, posuere luctus arcu. Fusce accumsan neque vel augue...</p>
    <time>On Dec 15, 2012</time>
  </article>
  <a class="read-all abs" style="left:1060px;top:894px;color:#fff">Read all...</a>

  <footer class="footer abs"></footer>

  <div class="panel abs" style="left:248px;width:372px"></div>
  <div class="tab abs cond" style="left:150px;padding:20px 0 0 9px">Clients<br><span style="padding-left:21px">Speaks</span></div>
  <div class="tab-pointer abs" style="left:248px"></div>
  <a class="read-all abs" style="left:184px;top:1096px;color:#fff;text-decoration:none">Read all...</a>
  <blockquote class="quote abs">“ sed pharetra et, gravida nec sem. Sed lectus dui, rutrum ac imperdiet eu, vulputate non purus. Duis ac eros sit amet nisi accused pharetra et, gravida nec sem. Sed lectus dui, rutrum ac imperdiet eu...”</blockquote>
  <p class="quote-by abs">Client Name, CEO,Company Name</p>

  <div class="panel abs" style="left:758px;width:372px"></div>
  <div class="tab abs cond" style="left:660px;padding:17px 0 0 16px">Register<br><span style="padding-left:21px">Today</span></div>
  <div class="tab-pointer abs" style="left:758px"></div>
  <p class="promise abs cond" style="left:791px;top:978px">No Commissions</p>
  <p class="promise abs cond" style="left:898px;top:1017px">No Fees</p>
  <a class="cta abs cond">REGISTER TODAY!<span class="cta-icon"><svg width="7" height="8" viewBox="0 0 7 8"><path d="M1 0l6 4-6 4z" fill="#0b7fd9"/></svg></span></a>

  <p class="footer-links abs">Home &nbsp;/ &nbsp;About &nbsp;/ &nbsp;Loans &nbsp;/ &nbsp;Contact</p>
  <p class="copyright abs">© 2012 Bramley.com. All rights reserved. &nbsp; / &nbsp; Privacy policy &nbsp; / &nbsp; Terms and conditions</p>
  <span class="social abs" style="left:1060px"></span>
  <span class="social abs" style="left:1099px"></span>
</div>
</body>
</html>
```